Business Card Design

I design and sell kitchens. I would like the card to have a black background either gloss or matt and a stripe through the middle in deep sky blue, the same blue as the team lark pro cycling team. Written in the blue stripe in white i would like Meridian kitchens in italics. underneath the stripe, again in white i would like 'the complete design and installation service. On the reverse i would like the following in simple black on white
Dean Marwick
07841 296054
email- deanmarwick@meridiankitchens-example.co.uk
Web- WWW.meridiankitchens-example.co.uk

I have added a copy of an initial idea for a logo but it can be changed to suit the brief above

Industry/Entity Type

Business

Contact Information for Business Card

Meridian Kitchens
The complete design and installation service
Dean Marwick
07841 296054-mob
deanmarwick@meridiankitchen-example.co.uk
WWW.meridiankitchens-example.co.uk

```html
<!DOCTYPE html>
<html lang="en">
<head>
<meta charset="utf-8">
<title>Meridian Kitchens – Business Card</title>
<link rel="stylesheet" href="https://fonts.googleapis.com/css2?family=Arvo&family=Tinos:ital,wght@0,400;0,700;1,400&display=swap">
<style>
  :root {
    --backdrop: #d9d9d9;
    --card-black: #060606;
    --card-white: #ffffff;
    --ink-white: #ffffff;
    --ink-black: #111111;
    --sky-blue: #1aa3df;
    --rule-grey: #8a8a8a;
  }
  * { margin: 0; padding: 0; box-sizing: border-box; }
  html, body { width: 1200px; height: 900px; overflow: hidden; }
  body { background: var(--backdrop); position: relative; }

  .card {
    position: absolute;
    top: 292px;
    width: 520px;
    height: 315px;
    overflow: hidden;
    box-shadow: 0 6px 18px rgba(0,0,0,0.25);
  }

  /* Front */
  .card--front { left: 50px; background: var(--card-black); }
  .brand-stripe {
    position: absolute;
    left: 0; right: 0; top: 118px; height: 76px;
    background: var(--sky-blue);
    display: flex; align-items: center; justify-content: center; gap: 14px;
  }
  .brand__square { width: 12px; height: 12px; background: var(--ink-white); }
  .brand__name {
    font-family: "Arvo", serif;
    font-size: 40px;
    line-height: 1;
    color: var(--ink-white);
    letter-spacing: 0.5px;
  }
  .tagline {
    position: absolute;
    left: 0; right: 0; top: 216px;
    text-align: center;
    font-family: "Tinos", serif;
    font-style: italic;
    font-size: 17px;
    color: var(--ink-white);
  }

  /* Back */
  .card--back { left: 630px; background: var(--card-white); }
  .accent-rule { position: absolute; display: block; }
  .accent-rule--top { left: 40px; top: 62px; }
  .accent-rule--bottom { left: 300px; top: 214px; }
  .contact-name {
    position: absolute; left: 40px; top: 80px;
    font-family: "Tinos", serif; font-weight: 700;
    font-size: 30px; line-height: 36px; color: var(--ink-black);
  }
  .contact-line {
    font-family: "Tinos", serif; font-size: 13px; color: var(--ink-black);
  }
  .contact-line .label { color: var(--ink-black); }
  .contact-mobile { position: absolute; left: 40px; top: 120px; }
  .contact-online {
    position: absolute; right: 40px; top: 172px;
    text-align: right; line-height: 18px;
  }
</style>
</head>
<body>

  <section class="card card--front" aria-label="Business card front">
    <div class="brand-stripe">
      <span class="brand__square"></span>
      <span class="brand__name">Meridian Kitchens</span>
    </div>
    <p class="tagline">the complete design and installation service</p>
  </section>

  <section class="card card--back" aria-label="Business card back">
    <svg class="accent-rule accent-rule--top" width="180" height="10" viewBox="0 0 180 10">
      <rect x="0" y="0" width="180" height="5" fill="var(--sky-blue)"/>
      <line x1="0" y1="8" x2="180" y2="8" stroke="var(--rule-grey)" stroke-width="1" stroke-dasharray="2 2"/>
    </svg>
    <h1 class="contact-name">Dean Marwick</h1>
    <p class="contact-line contact-mobile"><span class="label">mobile:</span> 07841 296054</p>
    <div class="contact-line contact-online">
      <p><span class="label">web:</span> www.meridiankitchens-example.co.uk</p>
      <p><span class="label">email:</span> deanmarwick@meridiankitchens-example.co.uk</p>
    </div>
    <svg class="accent-rule accent-rule--bottom" width="180" height="18" viewBox="0 0 180 18">
      <line x1="0" y1="3" x2="180" y2="3" stroke="var(--rule-grey)" stroke-width="1" stroke-dasharray="2 2"/>
      <rect x="0" y="11" width="180" height="5" fill="var(--sky-blue)"/>
    </svg>
  </section>

</body>
</html>
```